App design for timesheet system (desgn in Figma)

I am currently looking for a designer to design an app for my company. I run a labour hire/recruitment company and the app submits timesheets/timecards on a weekly basis.

PLEASE USE MY CURRENT THEME. I WOULD ONLY LIKE SUBMISSIONS USING MY THEME OF THE RED TRIANGLES/GRAY TRIANGLES. USE MY COLOURS.

(PAGE 1)
Loading/Landing page, logo with my theme incorporated in the page (AS PER ATTACHMENT)

(PAGE 2)
A dynamic changing page. This page changes according to the submissions (all of these are required for development). Using MY THEME, the functionality will be as follows:
- Ability to add companies and link different jobsites to them (sprites for adding company).
- The third page lists all the companies with jobsites as drop down. This must also have a 'calendar' (pn the top) or some sort of form where you can change the week you are submitting the timesheets for. We usually go by the Sunday and refer to it as WE (Week Ending).

(PAGE 3)
- When you tap on a jobsite, take you to a new page where you can attach multiple photos from your photo library. Ability to also write notes. The photos and notes save automatically when added, then a button to 'Send' which;
- Sends photos attached to an email to our TIMESHEETS email.
- The email subject will be '[COMPANY] - [JOBSITE] - [WE DATE]' and the body of the email will have [NOTES].
- Once a timesheet is submitted, a checkmark is added next to the jobsite for that week. (BACK TO PAGE 2, ADDING CHECKMARK)
- Able to send photos from photo library, messages or flocknet directly to the app under 'share'. Once the app is tapped from share photo, it will take you to the 'allocation' page where all the companies and jobsites are and you choose the jobsite to allocate to. This will not send to email yet but rather save in the app.

To simply,
1. Landing Page (loading)
2. Companies/jobsites page
- Add (DD.MM.YY - DD.MM.YY) to the top to signify the week we are referring to. This could be beside the calendar.
- Each rectangle below the dates should have "COMPANY NAME", this is a rectangle that will be a drop-down to display different jobsites.
- The jobsites will be 'sub-menus' so indent them a little.
- There are no buttons on this page.
- The 'jobsites' sub-menu will take you to the 3rd page
- There should be 'ticks' similar to Pingbox ticks for 'delivered, sent, seen'.
- These ticks will be '1. Photos Attached, 2. Submitted Timesheets, 3. Timesheets Sent'
3. Timesheet submission
- This page will be where the photos are submitted.
- At the top, there should be a button that says 'SUBMITTED TIMESHEETS' this will take you to the 4th page.
- Form for 'ATTACH FILE' (UPLOAD)
- Form for Notes
- Button to 'SUBMIT'
- The submit button will then go to the 4th page.
4. Timesheet display & Send
- The submitted timesheets are in rectangle and should be displayed in a matter of '1. COMPANY-JOBSITE', '2. COMPANY-JOBSITE'
- Similar to the dropdown boxes from page 2, these rectangles should have a dropdown and display the timesheet preview. When tapped on, the timesheet will expand in view.
- This page should have a "SUBMIT TIMESHEETS' button which will:
- Submit the timesheets, this will be sent to an email as described in the brief above.

```html
<!DOCTYPE html>
<html lang="en">
<head>
<meta charset="utf-8">
<title>Keystone Crew – Timesheet App Screens</title>
<link rel="stylesheet" href="https://fonts.googleapis.com/css2?family=Poppins:wght@400;500;600;700&display=swap">
<style>
  :root {
    --maroon: #7c1621;
    --maroon-deep: #4d0c18;
    --maroon-soft: #8f1c28;
    --ink: #2b2b2b;
    --muted: #9a9a9a;
    --line: #e6e6e6;
    --surface: #ffffff;
    --surface-alt: #f6f6f6;
    --stage: #ececec;
  }
  * { box-sizing: border-box; margin: 0; padding: 0; }
  html, body { width: 899px; height: 1200px; overflow: hidden; }
  body {
    background: var(--stage);
    font-family: "Poppins", sans-serif;
    color: var(--ink);
    position: relative;
  }
  .screen {
    position: absolute;
    width: 205px;
    height: 447px;
    background: var(--surface);
    border-radius: 26px;
    overflow: hidden;
    box-shadow: 0 18px 40px rgba(0,0,0,.12);
  }
  .screen--splash { left: 18px; top: 420px; }
  .screen--search { left: 237px; top: 355px; }
  .screen--submit { left: 456px; top: 420px; }
  .screen--sheets { left: 675px; top: 355px; }

  .status-bar {
    position: absolute; top: 8px; left: 14px; right: 14px;
    display: flex; justify-content: space-between; align-items: center;
    font-size: 7px; font-weight: 600; color: var(--ink);
  }
  .status-icons { display: flex; gap: 3px; align-items: center; }
  .notch {
    position: absolute; top: 0; left: 50%; transform: translateX(-50%);
    width: 96px; height: 16px; background: var(--stage);
    border-radius: 0 0 12px 12px;
  }
  .home-bar {
    position: absolute; bottom: 6px; left: 50%; transform: translateX(-50%);
    width: 72px; height: 2px; border-radius: 2px; background: #c8c8c8;
  }
  .icon-btn {
    position: absolute; top: 34px; width: 19px; height: 19px;
    border: 1px solid var(--line); border-radius: 5px; background: var(--surface);
    display: flex; align-items: center; justify-content: center;
  }
  .icon-btn--back { left: 14px; }
  .icon-btn--filter { right: 14px; }
  .screen-title {
    position: absolute; top: 36px; left: 0; right: 0; text-align: center;
    font-size: 12px; font-weight: 600; color: var(--ink);
  }

  /* splash */
  .brand {
    position: absolute; top: 50%; left: 50%; transform: translate(-50%,-50%);
    display: flex; align-items: center; gap: 6px;
  }
  .brand-mark { width: 10px; height: 10px; background: var(--maroon); }
  .brand-name { font-size: 16px; font-weight: 600; color: var(--maroon); white-space: nowrap; }

  /* search */
  .greeting { position: absolute; top: 74px; left: 19px; font-size: 7px; }
  .search-title { position: absolute; top: 86px; left: 19px; font-size: 13px; font-weight: 700; color: var(--maroon); }
  .search-lede { position: absolute; top: 106px; left: 19px; right: 22px; font-size: 6.5px; line-height: 1.45; color: #555; }
  .filter-panel {
    position: absolute; top: 148px; left: 0; right: 0; bottom: 0;
    border-radius: 22px 22px 26px 26px;
    background: linear-gradient(135deg, var(--maroon-soft), var(--maroon) 55%, var(--maroon-deep));
    color: #fff; padding: 16px 20px 0;
  }
  .field-label { font-size: 7px; margin-bottom: 6px; }
  .date-row { display: flex; align-items: center; gap: 6px; margin-bottom: 12px; }
  .date-box {
    width: 70px; height: 19px; background: var(--surface); border-radius: 3px;
    font-size: 6px; color: #555; display: flex; align-items: center; justify-content: space-between; padding: 0 5px;
  }
  .date-to { font-size: 6px; color: #d8a4aa; }
  .select-box {
    height: 19px; background: var(--surface); border-radius: 3px;
    font-size: 7px; color: var(--maroon); display: flex; align-items: center; justify-content: space-between; padding: 0 7px;
  }
  .option-list { margin-top: 4px; background: var(--surface); border-radius: 3px; padding: 2px 10px; }
  .option-list li { list-style: none; font-size: 7px; color: var(--ink); padding: 4px 0; border-bottom: 1px solid var(--line); }
  .option-list li:last-child { border-bottom: 0; }
  .status-list { margin-top: 14px; padding-left: 3px; }
  .status-row { display: flex; justify-content: space-between; align-items: center; font-size: 7px; margin-bottom: 10px; }
  .tick-box { width: 9px; height: 9px; background: var(--surface); border-radius: 2px; display: flex; align-items: center; justify-content: center; }
  .fab {
    position: absolute; right: 14px; bottom: 16px; width: 26px; height: 26px; border-radius: 50%;
    background: #b3202c; display: flex; align-items: center; justify-content: center;
  }
  .home-bar--light { background: rgba(255,255,255,.8); }

  /* shared red bars */
  .red-bar {
    position: absolute; left: 13px; right: 13px; height: 30px; border-radius: 3px;
    background: linear-gradient(90deg, var(--maroon), var(--maroon-deep));
    color: #fff; font-size: 7.5px; font-weight: 500;
    display: flex; align-items: center; justify-content: space-between; padding: 0 11px;
    box-shadow: 0 4px 8px rgba(0,0,0,.15);
  }

  /* submit */
  .upload-card {
    position: absolute; top: 165px; left: 13px; right: 13px; height: 240px;
    background: var(--surface); box-shadow: 0 3px 12px rgba(0,0,0,.07); border-radius: 3px;
  }
  .upload-card h3 { font-size: 8.5px; font-weight: 500; padding: 12px 13px 8px; border-bottom: 1px solid var(--line); }
  .file-row {
    margin: 8px 9px 0; height: 56px; background: var(--surface-alt); border-radius: 3px;
    display: flex; align-items: center; gap: 9px; padding: 0 10px; position: relative;
  }
  .file-thumb { width: 36px; height: 26px; background: linear-gradient(135deg, #f2f2f2, #cfcfcf); border-radius: 2px; }
  .file-name { font-size: 7.5px; }
  .file-state { font-size: 6.5px; color: var(--muted); }
  .file-remove { position: absolute; right: 14px; top: 27px; width: 6px; height: 6px; border-radius: 50%; background: #bdbdbd; }
  .add-row { height: 56px; }
  .add-slot { width: 30px; height: 34px; border: 1px dashed #b8b8b8; border-radius: 3px; display: flex; align-items: center; justify-content: center; }
  .add-label { font-size: 7px; color: var(--muted); }
  .note-input {
    margin: 8px 0 0; height: 30px; border: 1px solid var(--line); border-radius: 3px;
    font-size: 7px; color: var(--muted); display: flex; align-items: center; padding: 0 13px;
  }
  .primary-btn {
    position: absolute; left: 19px; right: 19px; height: 28px; border-radius: 3px;
    background: linear-gradient(90deg, var(--maroon), #6a101b); color: #fff;
    font-size: 7.5px; font-weight: 600; display: flex; align-items: center; justify-content: center;
    box-shadow: 0 4px 8px rgba(0,0,0,.18);
  }

  /* timesheets */
  .preview-card {
    position: absolute; top: 197px; left: 13px; right: 13px; height: 108px;
    background: var(--surface); box-shadow: 0 3px 12px rgba(0,0,0,.08); border-radius: 3px; padding: 10px 11px;
  }
  .preview-card h3 { font-size: 8px; font-weight: 500; margin-bottom: 8px; }
  .preview-image { height: 68px; background: linear-gradient(160deg, #f7f7f7, #d6d6d6 70%, #e9e3e4); border-radius: 2px; }
</style>
</head>
<body>

<!-- Splash -->
<section class="screen screen--splash" aria-label="Loading screen">
  <div class="notch"></div>
  <div class="status-bar"><span>9:41</span><span class="status-icons">
    <svg width="9" height="6" viewBox="0 0 9 6"><rect x="0" y="4" width="1.5" height="2" fill="#2b2b2b"/><rect x="2.5" y="3" width="1.5" height="3" fill="#2b2b2b"/><rect x="5" y="1.5" width="1.5" height="4.5" fill="#2b2b2b"/><rect x="7.5" y="0" width="1.5" height="6" fill="#2b2b2b"/></svg>
    <svg width="12" height="6" viewBox="0 0 12 6"><rect x=".5" y=".5" width="10" height="5" rx="1" fill="none" stroke="#2b2b2b"/><rect x="2" y="2" width="7" height="2" fill="#2b2b2b"/></svg>
  </span></div>
  <div class="brand"><span class="brand-mark"></span><span class="brand-name">Keystone Crew</span></div>
  <div class="home-bar"></div>
</section>

<!-- Search -->
<section class="screen screen--search" aria-label="Job search screen">
  <div class="notch"></div>
  <div class="status-bar"><span>9:41</span><span class="status-icons">
    <svg width="9" height="6" viewBox="0 0 9 6"><rect x="0" y="4" width="1.5" height="2" fill="#2b2b2b"/><rect x="2.5" y="3" width="1.5" height="3" fill="#2b2b2b"/><rect x="5" y="1.5" width="1.5" height="4.5" fill="#2b2b2b"/><rect x="7.5" y="0" width="1.5" height="6" fill="#2b2b2b"/></svg>
    <svg width="12" height="6" viewBox="0 0 12 6"><rect x=".5" y=".5" width="10" height="5" rx="1" fill="none" stroke="#2b2b2b"/><rect x="2" y="2" width="7" height="2" fill="#2b2b2b"/></svg>
  </span></div>
  <div class="icon-btn icon-btn--back"><svg width="6" height="8" viewBox="0 0 6 8"><path d="M5 1 2 4l3 3" fill="none" stroke="#7c1621" stroke-width="1.5"/></svg></div>
  <div class="icon-btn icon-btn--filter"><svg width="10" height="10" viewBox="0 0 10 10" stroke="#7c1621" stroke-width="1"><path d="M2 0v10M5 0v10M8 0v10"/><path d="M0.5 3h3M3.5 7h3M6.5 4h3"/></svg></div>
  <p class="greeting">Hello Dylan!</p>
  <h1 class="search-title">Search Your Job Here</h1>
  <p class="search-lede">Search for an open job, we may have the perfect position for you!</p>
  <div class="filter-panel">
    <p class="field-label">Select Date</p>
    <div class="date-row">
      <div class="date-box">14 / 01 / 21 <svg width="7" height="7" viewBox="0 0 7 7"><rect x=".5" y=".5" width="6" height="6" rx="1" fill="none" stroke="#7c1621"/></svg></div>
      <span class="date-to">To</span>
      <div class="date-box">15 / 01 / 21 <svg width="7" height="7" viewBox="0 0 7 7"><rect x=".5" y=".5" width="6" height="6" rx="1" fill="none" stroke="#7c1621"/></svg></div>
    </div>
    <p class="field-label">Select Company</p>
    <div class="select-box">Company Name <svg width="7" height="5" viewBox="0 0 7 5"><path d="M1 1l2.5 2.5L6 1" fill="none" stroke="#7c1621" stroke-width="1.2"/></svg></div>
    <ul class="option-list"><li>Sub Company</li><li>Sub Company</li><li>Sub Company</li></ul>
    <div class="status-list">
      <div class="status-row">Photos Attached <span class="tick-box"><svg width="7" height="6" viewBox="0 0 7 6"><path d="M1 3l2 2 3-4" fill="none" stroke="#7c1621" stroke-width="1.2"/></svg></span></div>
      <div class="status-row">Submitted Timesheets <span class="tick-box"></span></div>
      <div class="status-row">Timesheets Sent <span class="tick-box"></span></div>
    </div>
    <div class="fab"><svg width="12" height="12" viewBox="0 0 12 12"><path d="M6 1v10M1 6h10" stroke="#fff" stroke-width="1.4"/></svg></div>
  </div>
  <div class="home-bar home-bar--light"></div>
</section>

<!-- Submit -->
<section class="screen screen--submit" aria-label="Submit timesheet screen">
  <div class="notch"></div>
  <div class="status-bar"><span>9:41</span><span class="status-icons">
    <svg width="9" height="6" viewBox="0 0 9 6"><rect x="0" y="4" width="1.5" height="2" fill="#2b2b2b"/><rect x="2.5" y="3" width="1.5" height="3" fill="#2b2b2b"/><rect x="5" y="1.5" width="1.5" height="4.5" fill="#2b2b2b"/><rect x="7.5" y="0" width="1.5" height="6" fill="#2b2b2b"/></svg>
    <svg width="12" height="6" viewBox="0 0 12 6"><rect x=".5" y=".5" width="10" height="5" rx="1" fill="none" stroke="#2b2b2b"/><rect x="2" y="2" width="7" height="2" fill="#2b2b2b"/></svg>
  </span></div>
  <div class="icon-btn icon-btn--back"><svg width="6" height="8" viewBox="0 0 6 8"><path d="M5 1 2 4l3 3" fill="none" stroke="#7c1621" stroke-width="1.5"/></svg></div>
  <h2 class="screen-title">Submit Timesheet</h2>
  <div class="icon-btn icon-btn--filter"><svg width="10" height="10" viewBox="0 0 10 10" stroke="#7c1621" stroke-width="1"><path d="M2 0v10M5 0v10M8 0v10"/><path d="M0.5 3h3M3.5 7h3M6.5 4h3"/></svg></div>
  <div class="red-bar" style="top:98px">Submitted Timesheets <svg width="8" height="9" viewBox="0 0 8 9"><rect x=".5" y=".5" width="7" height="8" fill="none" stroke="#fff"/><path d="M2 3h4M2 5h4M2 7h3" stroke="#fff"/></svg></div>
  <div class="red-bar" style="top:133px">+Attach File <svg width="7" height="9" viewBox="0 0 7 9"><path d="M0 0h5l2 2v7H0z" fill="#fff"/><path d="M3.5 3v4M1.5 5h4" stroke="#7c1621"/></svg></div>
  <div class="upload-card">
    <h3>Upload Timesheets</h3>
    <div class="file-row">
      <div class="file-thumb" role="img" aria-label="Thumbnail of the uploaded weekly time sheet"></div>
      <div><p class="file-name">Weekly Timesheet</p><p class="file-state">Uploading...</p></div>
      <span class="file-remove"></span>
    </div>
    <div class="file-row add-row">
      <div class="add-slot"><svg width="14" height="14" viewBox="0 0 14 14" fill="none" stroke="#9a9a9a"><rect x="1" y="1" width="5" height="5"/><rect x="8" y="1" width="5" height="5"/><rect x="8" y="8" width="5" height="5"/><path d="M3.5 8v5M1 10.5h5"/></svg></div>
      <span class="add-label">Add More +</span>
    </div>
    <div class="note-input">Add Note</div>
  </div>
  <div class="primary-btn" style="top:390px">Submit</div>
  <div class="home-bar"></div>
</section>

<!-- Timesheets -->
<section class="screen screen--sheets" aria-label="Timesheets list screen">
  <div class="notch"></div>
  <div class="status-bar"><span>9:41</span><span class="status-icons">
    <svg width="9" height="6" viewBox="0 0 9 6"><rect x="0" y="4" width="1.5" height="2" fill="#2b2b2b"/><rect x="2.5" y="3" width="1.5" height="3" fill="#2b2b2b"/><rect x="5" y="1.5" width="1.5" height="4.5" fill="#2b2b2b"/><rect x="7.5" y="0" width="1.5" height="6" fill="#2b2b2b"/></svg>
    <svg width="12" height="6" viewBox="0 0 12 6"><rect x=".5" y=".5" width="10" height="5" rx="1" fill="none" stroke="#2b2b2b"/><rect x="2" y="2" width="7" height="2" fill="#2b2b2b"/></svg>
  </span></div>
  <div class="icon-btn icon-btn--back"><svg width="6" height="8" viewBox="0 0 6 8"><path d="M5 1 2 4l3 3" fill="none" stroke="#7c1621" stroke-width="1.5"/></svg></div>
  <h2 class="screen-title">Timesheets</h2>
  <div class="icon-btn icon-btn--filter"><svg width="10" height="10" viewBox="0 0 10 10" stroke="#7c1621" stroke-width="1"><path d="M2 0v10M5 0v10M8 0v10"/><path d="M0.5 3h3M3.5 7h3M6.5 4h3"/></svg></div>
  <div class="red-bar" style="top:95px">01. Company-Jobsite <svg width="7" height="5" viewBox="0 0 7 5"><path d="M1 1l2.5 2.5L6 1" fill="none" stroke="#fff" stroke-width="1.1"/></svg></div>
  <div class="red-bar" style="top:129px">02. Company-Jobsite <svg width="7" height="5" viewBox="0 0 7 5"><path d="M1 1l2.5 2.5L6 1" fill="none" stroke="#fff" stroke-width="1.1"/></svg></div>
  <div class="red-bar" style="top:163px">03. Company-Jobsite <svg width="7" height="5" viewBox="0 0 7 5"><path d="M1 1l2.5 2.5L6 1" fill="none" stroke="#fff" stroke-width="1.1"/></svg></div>
  <div class="preview-card">
    <h3>Timesheet Preview</h3>
    <div class="preview-image" role="img" aria-label="Photo of a printed weekly time sheet with a pen"></div>
  </div>
  <div class="primary-btn" style="top:393px;left:13px;right:13px">Submit Timesheets</div>
  <div class="home-bar"></div>
</section>

</body>
</html>
```